Letterhead Design Project

Please see attached logo as well as information below which could be relevant to design. Let me know if you have any questions.

Derek J. Vollman
Estate Planning and Insurance Specialist
Dvollman@vollmanadvisory.com
P: 516-298-4153 F: 516-298-4187
www.vollmanadvisory.com
4150 Brindlemoor Parkway, Suite 317E
Syosset, New York 11804

Insurance

```html
<!DOCTYPE html>
<html lang="en">
<head>
<meta charset="utf-8">
<title>Vollman Advisory Letterhead</title>
<link rel="stylesheet" href="https://fonts.googleapis.com/css2?family=Source+Sans+3:wght@400;600;700&display=swap">
<style>
  :root {
    --backdrop: #000000;
    --paper: #ffffff;
    --slate: #333d45;
    --gold: #c4ad7c;
    --ink: #1a1a1a;
    --mark: #231f20;
  }
  html, body {
    margin: 0;
    padding: 0;
    width: 1200px;
    height: 1200px;
    overflow: hidden;
    background: var(--backdrop);
  }
  .canvas {
    position: relative;
    width: 1200px;
    height: 1200px;
    font-family: "Source Sans 3", "Myriad Pro", Arial, sans-serif;
    color: var(--ink);
  }
  .frame-shapes {
    position: absolute;
    inset: 0;
  }
  .brand-mark {
    position: absolute;
    left: 737px;
    top: 137px;
    width: 72px;
    height: 72px;
    background: var(--mark);
    display: flex;
    align-items: center;
    justify-content: center;
    text-align: center;
    color: var(--gold);
    font-weight: 600;
    font-size: 11px;
    line-height: 1.2;
  }
  .contact-block {
    position: absolute;
    left: 831px;
    top: 134px;
    width: 140px;
    font-size: 9.6px;
    line-height: 12.4px;
  }
  .contact-block p {
    margin: 0;
  }
  .contact-name {
    font-size: 12.5px;
    font-weight: 700;
    line-height: 15px;
  }
  .contact-gap {
    margin-top: 13px !important;
  }
  .contact-label {
    font-weight: 700;
  }
  .website {
    position: absolute;
    right: 244px;
    top: 1065px;
    font-size: 10.5px;
    font-weight: 700;
  }
</style>
</head>
<body>
<div class="canvas">
  <svg class="frame-shapes" width="1200" height="1200" viewBox="0 0 1200 1200" aria-hidden="true">
    <rect class="page" x="193" y="71" width="814" height="1056" fill="var(--paper)"/>
    <polygon class="header-band" points="764,71 1007,71 1007,260 967,287 967,101 737,101" fill="var(--slate)"/>
    <polyline class="header-rule" points="737,103 965,103 965,287" fill="none" stroke="var(--gold)" stroke-width="4"/>
    <polygon class="footer-band" points="193,1073 221,1073 221,1099 977,1099 977,1073 1007,1073 1007,1127 193,1127" fill="var(--slate)"/>
    <polyline class="footer-rule" points="225,1073 225,1095 973,1095 973,1073" fill="none" stroke="var(--gold)" stroke-width="4"/>
  </svg>

  <div class="brand-mark">Vollman<br>Advisory</div>

  <div class="contact-block">
    <p class="contact-name">Derek J. Vollman</p>
    <p>Estate Planning and<br>Insurance Specialist</p>
    <p class="contact-gap">Dvollman@vollmanadvisory.com</p>
    <p><span class="contact-label">P.</span> 516-298-4153</p>
    <p><span class="contact-label">F.</span> 516-298-4187</p>
    <p class="contact-gap">4150 Brindlemoor Parkway<br>Suite 317E, Syosset<br>New York 11804</p>
  </div>

  <div class="website">www.vollmanadvisory.com</div>
</div>
</body>
</html>
```